Innovative Freezer Label Design

Create a versatile and innovative freezer label design with universal appeal, suitable for different functionalities. The design should cater to a diverse audience, including those who freeze meals for meal prepping, batch cooking, and the restaurant industry. Our vision is a visually striking and distinctive design that embodies simplicity.

Example "our current labels feature essential details like "Contents" and "Date." We recognize these as crucial points of information. Currently, the challenge lies in creating various labels for different marketplaces, considering language barriers. A proposed solution involves the integration of universal icons to replace specific words, promoting practicality for international sales."

Kindly note that design concepts should not be restricted to our current product, brand guideline, logo, or the provided example.

Our goal is not only product differentiation but also increased sales through a blend of functionality and aesthetics.

The following are examples of freezer labels designs. Kindly do not restrict your designs to the examples. The designs must be universal (for language barrier purposes)

Examples:
https://www.tackvora.co.uk/pin/5827164039281736401/
https://www.tackvora.co.uk/pin/5827164039281736405/
https://www.tackvora.co.uk/pin/5827164039281736394/
https://www.tackvora.co.uk/pin/5827164039281736308/
https://www.tackvora.co.uk/pin/5827164039281797750/

Please reach out if you have any questions.

Thank you

```html
<!DOCTYPE html>
<html lang="en">
<head>
<meta charset="utf-8">
<title>Freezer Label – Kelvo Cold Store</title>
<link rel="stylesheet" href="https://fonts.googleapis.com/css2?family=Arimo&display=swap">
<style>
  :root {
    --forest: #03272a;
    --paper: #ffffff;
  }
  * { margin: 0; padding: 0; box-sizing: border-box; }
  html, body {
    width: 1200px;
    height: 755px;
    overflow: hidden;
    background: var(--forest);
  }
  .canvas {
    position: relative;
    width: 1200px;
    height: 755px;
    background: var(--forest);
  }
  .label {
    position: absolute;
    left: 145.5px;
    top: 150.5px;
    width: 909px;
    height: 454.5px;
    background: var(--paper);
    border-radius: 22px;
    overflow: hidden;
  }
  .field-icon {
    position: absolute;
    width: 72px;
    height: 72px;
  }
  .field-icon--contents { left: 28.5px; top: 41.5px; }
  .field-icon--date { left: 28.5px; top: 343.5px; }
  .date-slashes {
    position: absolute;
    left: 198px;
    top: 358px;
    width: 120px;
    height: 55px;
  }
  .brand {
    position: absolute;
    left: 648px;
    top: 318px;
    width: 230px;
    font-family: "Arimo", Arial, sans-serif;
    font-weight: 400;
    color: var(--forest);
    line-height: 1;
    white-space: nowrap;
  }
  .brand__name {
    display: block;
    font-size: 60px;
    letter-spacing: 4px;
  }
  .brand__line {
    display: block;
    margin-top: 7px;
    font-size: 28px;
    letter-spacing: 5px;
  }
  .note {
    position: absolute;
    left: 0;
    top: 648px;
    width: 1200px;
    text-align: center;
    font-family: "Arimo", Arial, sans-serif;
    font-size: 31px;
    color: var(--paper);
  }
</style>
</head>
<body>
<main class="canvas">
  <section class="label">
    <svg class="field-icon field-icon--contents" viewBox="-36 -36 72 72" aria-label="Contents">
      <circle r="33" fill="none" stroke="var(--forest)" stroke-width="4.5"/>
      <g fill="var(--forest)">
        <circle cx="-20" cy="-10" r="2.2"/>
        <circle cx="-20" cy="0" r="2.2"/>
        <circle cx="-20" cy="9" r="2.2"/>
        <rect x="-14" y="-12" width="35.5" height="4"/>
        <rect x="-14" y="-2" width="35.5" height="4"/>
        <rect x="-14" y="7" width="35.5" height="4"/>
      </g>
    </svg>

    <svg class="field-icon field-icon--date" viewBox="-36 -36 72 72" aria-label="Date">
      <circle r="33" fill="none" stroke="var(--forest)" stroke-width="4.5"/>
      <rect x="-16" y="-13" width="32" height="30" rx="2.5" fill="none" stroke="var(--forest)" stroke-width="2.2"/>
      <rect x="-16" y="-13" width="32" height="5" fill="var(--forest)"/>
      <g fill="none" stroke="var(--forest)" stroke-width="1.6">
        <rect x="-11.5" y="-18" width="2.6" height="6" rx="1.3" fill="var(--paper)"/>
        <rect x="-4.8" y="-18" width="2.6" height="6" rx="1.3" fill="var(--paper)"/>
        <rect x="1.9" y="-18" width="2.6" height="6" rx="1.3" fill="var(--paper)"/>
        <rect x="8.6" y="-18" width="2.6" height="6" rx="1.3" fill="var(--paper)"/>
      </g>
      <g fill="var(--forest)">
        <rect x="-11.5" y="-5" width="4" height="4"/><rect x="-5.5" y="-5" width="4" height="4"/><rect x="0.5" y="-5" width="4" height="4"/><rect x="6.5" y="-5" width="4" height="4"/>
        <rect x="-11.5" y="1" width="4" height="4"/><rect x="-5.5" y="1" width="4" height="4"/><rect x="0.5" y="1" width="4" height="4"/><rect x="6.5" y="1" width="4" height="4"/>
        <rect x="-11.5" y="7" width="4" height="4"/><rect x="-5.5" y="7" width="4" height="4"/><rect x="0.5" y="7" width="4" height="4"/><rect x="6.5" y="7" width="4" height="4"/>
      </g>
    </svg>

    <svg class="date-slashes" viewBox="0 0 120 55" aria-hidden="true">
      <polygon points="0,55 5,55 19,0 14,0" fill="var(--forest)"/>
      <polygon points="100,55 105,55 119,0 114,0" fill="var(--forest)"/>
    </svg>

    <div class="brand">
      <span class="brand__name">KELVO</span>
      <span class="brand__line">Cold Store</span>
    </div>
  </section>

  <p class="note">the label design covers the white box only</p>
</main>
</body>
</html>
```